Business Card Design Project

Keep it simple , using logo and colors that compliment. Logo on one side with complimentary back ground color. Other side, personal info with possible complimentary design/colors

Target Market(s)

we are a non for profit that will be seeking donations . Both monetary and in kind

Industry/Entity Type

Business

Font styles to use
Sans Serif

Colors

Designer to choose colors to be used in the design.

```html
<!DOCTYPE html>
<html lang="en">
<head>
<meta charset="UTF-8">
<title>Bright Shift – Business Card</title>
<link href="https://fonts.googleapis.com/css2?family=Open+Sans:wght@300;400;700&display=swap" rel="stylesheet">
<style>
  :root {
    --canvas-bg: #e9e9ea;
    --card-white: #ffffff;
    --card-pearl: #f4f4f2;
    --navy: #272d4d;
    --yellow: #e6cb00;
    --text-dark: #272d4d;
    --text-body: #2a2e3f;
  }
  * { box-sizing: border-box; margin: 0; padding: 0; }
  html, body {
    width: 1200px;
    height: 675px;
    overflow: hidden;
    background: var(--canvas-bg);
    font-family: "Open Sans", Arial, sans-serif;
  }
  .canvas {
    position: relative;
    width: 1200px;
    height: 675px;
    display: flex;
    align-items: center;
    justify-content: center;
    gap: 60px;
  }
  .card {
    position: relative;
    width: 520px;
    height: 297px;
    overflow: hidden;
    box-shadow: 0 6px 18px rgba(0, 0, 0, 0.12);
  }
  .card--front { background: var(--card-white); }
  .card--back { background: var(--card-pearl); }

  /* Brand name with a plain marker */
  .brand {
    display: flex;
    align-items: center;
    gap: 12px;
  }
  .brand__marker {
    border-radius: 50%;
    background: var(--yellow);
    flex: none;
  }
  .brand__name {
    font-weight: 300;
    color: var(--navy);
    white-space: nowrap;
  }
  .card--front .brand {
    position: absolute;
    inset: 0;
    justify-content: center;
  }
  .card--front .brand__marker { width: 18px; height: 18px; }
  .card--front .brand__name { font-size: 40px; }

  .card--back .brand {
    position: absolute;
    top: 40px;
    right: 34px;
    gap: 8px;
  }
  .card--back .brand__marker { width: 10px; height: 10px; }
  .card--back .brand__name { font-size: 22px; }

  /* Identity */
  .identity {
    position: absolute;
    top: 92px;
    left: 32px;
  }
  .identity__name {
    font-size: 15px;
    font-weight: 700;
    color: var(--text-dark);
  }
  .identity__role {
    font-size: 9px;
    color: var(--text-body);
    margin-top: 1px;
  }

  /* Contacts */
  .contacts {
    position: absolute;
    left: 32px;
    bottom: 44px;
    list-style: none;
    font-size: 11px;
    color: var(--text-body);
    line-height: 18px;
  }
  .contacts li { display: flex; align-items: center; gap: 10px; }
  .contacts svg { width: 10px; height: 10px; fill: var(--navy); flex: none; }
  .contacts .pair { display: flex; align-items: center; gap: 10px; }

  .swoosh {
    position: absolute;
    inset: 0;
    width: 100%;
    height: 100%;
  }
  .swoosh .band--yellow { fill: var(--yellow); }
  .swoosh .band--navy { fill: var(--navy); }
</style>
</head>
<body>
<main class="canvas">

  <section class="card card--front" aria-label="Card front">
    <div class="brand">
      <span class="brand__marker"></span>
      <span class="brand__name">Bright Shift</span>
    </div>
  </section>

  <section class="card card--back" aria-label="Card back">
    <svg class="swoosh" viewBox="0 0 520 297" preserveAspectRatio="none" aria-hidden="true">
      <path class="band--yellow" d="M150,297 C300,262 430,205 520,150 L520,168 C430,220 310,272 190,297 Z"/>
      <path class="band--navy" d="M120,297 C290,275 430,222 520,168 L520,297 Z"/>
    </svg>

    <div class="brand">
      <span class="brand__marker"></span>
      <span class="brand__name">Bright Shift</span>
    </div>

    <div class="identity">
      <p class="identity__name">Your Long Name</p>
      <p class="identity__role">Owner / President</p>
    </div>

    <ul class="contacts">
      <li>
        <svg viewBox="0 0 10 10"><path d="M5 0a3.5 3.5 0 0 0-3.5 3.5C1.5 6 5 10 5 10s3.5-4 3.5-6.5A3.5 3.5 0 0 0 5 0zm0 5a1.5 1.5 0 1 1 0-3 1.5 1.5 0 0 1 0 3z"/></svg>
        Your Commercial or office address
      </li>
      <li>
        <svg viewBox="0 0 10 10"><path d="M2 0.5l2 2-1 1.2c.6 1.3 1.6 2.3 2.9 2.9L7 5.6l2 2-1.2 1.6C4.5 9 1 5.5.6 2.2z"/></svg>
        <span class="pair">00.00.00.0000
          <svg viewBox="0 0 10 10"><path d="M2 0h5v3H2zM0 3.5h10V9H0zM2 5h2v1H2zm0 1.6h2v1H2zm4-1.6h2v2.6H6z"/></svg>
          00.00.00.0000</span>
      </li>
      <li>
        <svg viewBox="0 0 10 10"><path d="M0 2h10v6H0zm.8.6L5 5.6l4.2-3z" fill-rule="evenodd"/></svg>
        yourname@yourwebsite.com
      </li>
      <li>
        <svg viewBox="0 0 10 10"><path d="M5 0a5 5 0 1 0 0 10A5 5 0 0 0 5 0zm0 1c.6.6 1 1.6 1.2 3.5H3.8C4 2.6 4.4 1.6 5 1zM1.1 4.5a4 4 0 0 1 2-3.1c-.3.8-.5 1.9-.6 3.1zm0 1h1.5c.1 1.2.3 2.3.6 3.1a4 4 0 0 1-2.1-3.1zM5 9c-.6-.6-1-1.6-1.2-3.5h2.4C6 7.4 5.6 8.4 5 9zm1.9-.4c.3-.8.5-1.9.6-3.1h1.5a4 4 0 0 1-2.1 3.1zm.6-4.1c-.1-1.2-.3-2.3-.6-3.1a4 4 0 0 1 2 3.1z"/></svg>
        www.yourwebsite.com
      </li>
    </ul>
  </section>

</main>
</body>
</html>
```